Brell Harbor Company Business Cards

Front and Back Business Card - logo and text setup - cool design. I need workable photoshop or illustrator files so I can setup each employee card with design that is created
Updates

Hi everyone, thank you for the great entries. Please no more white and blue cards - there are so many already - black and silver only now please. thanks!

Target Market(s)

Construction Industry - Facility Managers

Industry/Entity Type

Construction

Contact Information for Business Card

I really like contemporary simplistic looks - clean neat....not opposed to seeing some black backrounds

Requirements
Must have
• Logo/website address with design on front only - www.brellharbor-example.com (logo attached)
• Back:
• Name/Title/Company Address/Phone/email address
Nice to have
• Cool design
Should not have
• Nothing gimmicky like Fire or Water - since we are a Fire Protection company - it has all been done

```html
<!DOCTYPE html>
<html lang="en">
<head>
<meta charset="utf-8">
<title>Brell Harbor Company – Business Cards</title>
<link href="https://fonts.googleapis.com/css2?family=Montserrat:wght@400;700;800&family=Raleway:wght@400;500&display=swap" rel="stylesheet">
<style>
  :root {
    --jet: #111214;
    --silver: #b9bdc2;
    --silver-light: #dcdfe2;
    --paper: #ffffff;
    --backdrop: #e4e6e7;
    --ink-on-dark: #f2f3f4;
    --ink-soft: #c4c8cc;
  }
  html, body {
    margin: 0;
    padding: 0;
    width: 1200px;
    height: 1200px;
    overflow: hidden;
    background: var(--backdrop);
  }
  .sheet {
    width: 1200px;
    height: 1200px;
    display: flex;
    flex-direction: column;
    align-items: center;
    justify-content: center;
    gap: 60px;
  }
  .card {
    position: relative;
    width: 840px;
    height: 480px;
    background: var(--paper);
    overflow: hidden;
    box-shadow: 0 10px 30px rgba(0,0,0,0.14);
  }
  .card-shapes {
    position: absolute;
    inset: 0;
    width: 100%;
    height: 100%;
  }
  .shape-dark { fill: var(--jet); }
  .shape-silver { fill: url(#silver-sheen); }
  .shape-silver-back { fill: url(#silver-sheen-back); }

  .wordmark {
    position: absolute;
    font-family: "Montserrat", sans-serif;
    font-weight: 800;
    color: var(--jet);
    letter-spacing: -0.5px;
    white-space: nowrap;
  }
  .card-front .wordmark {
    left: 0;
    right: 0;
    top: 140px;
    text-align: center;
    font-size: 54px;
    padding-right: 80px;
  }
  .card-back .wordmark {
    left: 44px;
    top: 238px;
    font-size: 32px;
  }
  .website {
    position: absolute;
    left: 120px;
    top: 392px;
    font-family: "Montserrat", sans-serif;
    font-weight: 700;
    font-size: 25px;
    color: var(--ink-on-dark);
    transform: rotate(4.3deg);
    transform-origin: left center;
    white-space: nowrap;
  }
  .contact-block {
    position: absolute;
    right: 44px;
    top: 40px;
    text-align: right;
    color: var(--ink-on-dark);
    font-family: "Raleway", sans-serif;
    font-size: 18px;
    line-height: 1.4;
  }
  .contact-block p { margin: 0; }
  .contact-name {
    font-family: "Montserrat", sans-serif;
    font-weight: 700;
    font-size: 26px;
  }
  .contact-title {
    color: var(--ink-soft);
    font-weight: 500;
  }
  .contact-group {
    margin-top: 24px !important;
  }
</style>
</head>
<body>
<main class="sheet">
  <section class="card card-front" aria-label="Business card front">
    <svg class="card-shapes" viewBox="0 0 840 480" preserveAspectRatio="none" aria-hidden="true">
      <defs>
        <linearGradient id="silver-sheen" x1="0" y1="0" x2="1" y2="1">
          <stop offset="0" stop-color="#e3e5e8"/>
          <stop offset="0.5" stop-color="#a9aeb4"/>
          <stop offset="1" stop-color="#cfd2d6"/>
        </linearGradient>
      </defs>
      <polygon class="shape-silver" points="440,378 840,340 840,412"/>
      <polygon class="shape-dark" points="0,345 840,410 840,480 0,480"/>
    </svg>
    <div class="wordmark">Brell Harbor</div>
    <div class="website">www.brellharbor-example.com</div>
  </section>

  <section class="card card-back" aria-label="Business card back">
    <svg class="card-shapes" viewBox="0 0 840 480" preserveAspectRatio="none" aria-hidden="true">
      <defs>
        <linearGradient id="silver-sheen-back" x1="0" y1="0" x2="0" y2="1">
          <stop offset="0" stop-color="#dfe2e5"/>
          <stop offset="0.55" stop-color="#a7acb2"/>
          <stop offset="1" stop-color="#c9ccd0"/>
        </linearGradient>
      </defs>
      <polygon class="shape-silver-back" points="372,190 470,480 410,480"/>
      <polygon class="shape-dark" points="345,0 840,0 840,480 480,480 384,180"/>
    </svg>
    <div class="wordmark">Brell Harbor</div>
    <div class="contact-block">
      <p class="contact-name">Dana Merrow Ellison</p>
      <p class="contact-title">President</p>
      <p class="contact-group">48 Quarry Lane<br>Westbrook Point, NY 10990</p>
      <p class="contact-group">T: (555) 014-2287<br>F: (555) 014-2290</p>
      <p class="contact-group">dana@brellharbor-example.com<br>info@brellharbor-example.com</p>
    </div>
  </section>
</main>
</body>
</html>
```